1923 Basins & Spouts Business Card

I'm wanting to get a business card designed. Our business is 1923 Basins & Spouts
Details for the card:

1923 Basins & Spouts
Name: Gareth Vostle
Email: gareth@1923basinsandspouts.com.au
Website: www.1923basinsandspouts.com.au
Mobile: 0439 602 158
Phone: 02 5550 1843

Font of Basins & Spouts is called Snell Roundhand. Not sue what font logo text is.

I'm thinking two sided but it doesn't have to be.

```html
<!DOCTYPE html>
<html lang="en">
<head>
<meta charset="utf-8">
<title>1923 Basins &amp; Spouts – Business Card</title>
<link rel="stylesheet" href="https://fonts.googleapis.com/css2?family=Lato:wght@400;700&display=swap">
<style>
  :root {
    --backdrop: #161616;
    --card: #262626;
    --card-edge: #303030;
    --ink: #f2f2f2;
    --ink-soft: #bdbdbd;
    --rule: #d9d9d9;
  }
  * { margin: 0; padding: 0; box-sizing: border-box; }
  html, body {
    width: 1200px;
    height: 900px;
    overflow: hidden;
    background: var(--backdrop);
    font-family: "Lato", sans-serif;
    color: var(--ink);
  }
  .stage {
    position: relative;
    width: 1200px;
    height: 900px;
  }
  .card {
    position: absolute;
    left: 290px;
    width: 620px;
    height: 379px;
    background: linear-gradient(135deg, var(--card-edge), var(--card));
    box-shadow: 0 18px 40px rgba(0,0,0,0.55);
  }
  .card--front { top: 50px; }
  .card--back { top: 471px; }

  .front-mark {
    position: absolute;
    inset: 0;
    display: flex;
    align-items: center;
    justify-content: center;
    font-size: 64px;
    font-weight: 400;
    letter-spacing: 2px;
    color: var(--ink);
  }

  .brand {
    position: absolute;
    left: 34px;
    top: 150px;
    width: 260px;
  }
  .brand__name {
    font-size: 21px;
    font-weight: 400;
    color: var(--ink);
    white-space: nowrap;
  }
  .brand__tagline {
    margin-top: 6px;
    font-size: 9px;
    color: var(--ink-soft);
    white-space: nowrap;
  }

  .divider {
    position: absolute;
    left: 306px;
    top: 72px;
    width: 1px;
    height: 226px;
    background: var(--rule);
  }

  .contact {
    position: absolute;
    left: 330px;
    top: 74px;
    width: 270px;
  }
  .contact__name {
    font-size: 23px;
    font-weight: 700;
    letter-spacing: 2.5px;
    text-transform: uppercase;
    line-height: 1.1;
  }
  .contact__role {
    font-size: 13px;
    letter-spacing: 0.5px;
    color: var(--ink-soft);
    margin-top: 2px;
  }
  .contact__address {
    margin-top: 16px;
    font-size: 14px;
    line-height: 1.3;
    font-style: normal;
    letter-spacing: 0.4px;
  }
  .contact__list {
    list-style: none;
    margin-top: 14px;
  }
  .contact__item {
    display: flex;
    align-items: center;
    gap: 8px;
    font-size: 14px;
    line-height: 21px;
    letter-spacing: 0.4px;
    white-space: nowrap;
  }
  .contact__icon {
    width: 12px;
    height: 12px;
    flex: none;
    fill: none;
    stroke: var(--ink);
    stroke-width: 1.4;
  }
</style>
</head>
<body>
<main class="stage">
  <section class="card card--front" aria-label="Card front">
    <div class="front-mark">1923</div>
  </section>

  <section class="card card--back" aria-label="Card back">
    <div class="brand">
      <div class="brand__name">1923 Basins &amp; Spouts</div>
      <div class="brand__tagline">Pairing lasting elegance with honest everyday function</div>
    </div>

    <div class="divider"></div>

    <div class="contact">
      <div class="contact__name">Gareth Vostle</div>
      <div class="contact__role">Director</div>
      <address class="contact__address">PO Box 48 Kelmore<br>Ridge NSW 2791</address>
      <ul class="contact__list">
        <li class="contact__item">
          <svg class="contact__icon" viewBox="0 0 12 12"><path d="M3 1 L4.6 3.6 L3.6 4.6 Q4.6 7 7.4 8.4 L8.4 7.4 L11 9 L9.8 11 Q4.5 10.5 1 2.2 Z"/></svg>
          <span>0439 602 158</span>
        </li>
        <li class="contact__item">
          <svg class="contact__icon" viewBox="0 0 12 12"><rect x="3" y="0.8" width="6" height="10.4" rx="1"/><line x1="5.2" y1="9.4" x2="6.8" y2="9.4"/></svg>
          <span>02 5550 1843</span>
        </li>
        <li class="contact__item">
          <svg class="contact__icon" viewBox="0 0 12 12"><rect x="0.8" y="2.5" width="10.4" height="7" /><polyline points="0.8,2.5 6,6.6 11.2,2.5"/></svg>
          <span>gareth@1923basinsandspouts.com.au</span>
        </li>
        <li class="contact__item">
          <svg class="contact__icon" viewBox="0 0 12 12"><circle cx="6" cy="6" r="5"/><ellipse cx="6" cy="6" rx="2.2" ry="5"/><line x1="1" y1="6" x2="11" y2="6"/></svg>
          <span>www.1923basinsandspouts.com.au</span>
        </li>
      </ul>
    </div>
  </section>
</main>
</body>
</html>
```